infographic about brain health and home health

We want one side to be about brain health and have our logo as well as the logo for Quillmere Vista Center, and then on the other side, all about home health care .... with our logo and our contact information.

```html
<!DOCTYPE html>
<html lang="en">
<head>
<meta charset="utf-8">
<title>Alderline HealthCare – Home Care &amp; Brain Health</title>
<link href="https://fonts.googleapis.com/css2?family=Allura&family=Roboto:ital,wght@0,400;0,500;0,700;1,400&display=swap" rel="stylesheet">
<style>
  :root{
    --teal:#5cc4c9;
    --teal-dark:#2a9aa0;
    --teal-light:#bfe9eb;
    --ink:#111213;
    --white:#ffffff;
    --stage:#b4b2c4;
    --text:#1c1d1f;
  }
  *{box-sizing:border-box;margin:0;padding:0}
  html,body{width:1200px;height:1200px;overflow:hidden;background:var(--stage);font-family:'Roboto',sans-serif;color:var(--text)}
  ul{list-style:none}
  .canvas{position:relative;width:1200px;height:1200px}
  .flyer{position:absolute;width:538px;height:762px;background:var(--white);overflow:hidden}
  .flyer--homecare{left:42px;top:34px}
  .flyer--brain{left:617px;top:394px;width:537px}
  .abs{position:absolute}
  .script{font-family:'Allura',cursive}

  /* Home care flyer */
  .hero-photo{left:0;top:60px;width:538px;height:238px;background:linear-gradient(160deg,#9aa3a2 0%,#6f6a5f 45%,#4a4640 70%,#8d8c88 100%)}
  .header-art{left:0;top:0}
  .brand-mark{left:22px;top:88px;width:170px;text-align:center;color:var(--white)}
  .brand-mark__name{font-size:13px;letter-spacing:9px;font-weight:400}
  .brand-mark__sub{font-size:5px;letter-spacing:4px;margin-top:6px}
  .home-title{right:24px;top:8px;color:var(--white);font-size:56px;line-height:1}
  .vision{left:0;top:298px;width:538px;height:60px;background:var(--teal);font-size:10.4px;line-height:1.25;text-align:center;padding:9px 14px 0;color:var(--text)}
  .audience{left:10px;top:372px;width:232px;text-align:center}
  .audience__lead{font-size:33px;color:var(--teal-dark);line-height:.9}
  .audience__title{font-size:14.5px;font-weight:500;margin-top:2px}
  .audience__rule{display:block;margin:2px auto 10px}
  .audience__people{font-size:14.5px;font-weight:500}
  .audience__list{font-size:11.7px;line-height:1.4}
  .audience__list em{font-style:normal;color:var(--teal-dark)}
  .care-illustration{left:26px;top:554px;width:184px;height:142px;border-radius:8px;background:linear-gradient(180deg,#d3f0f1,#8fd6da)}
  .benefits{left:247px;top:371px;width:280px;height:309px;background:var(--ink);border:2px solid var(--teal);border-radius:16px;color:var(--white)}
  .benefits__head{text-align:center;margin-top:4px}
  .benefits__lead{font-size:34px;color:var(--teal);line-height:.9}
  .benefits__title{font-size:14px;font-weight:500;letter-spacing:.2px}
  .benefits__grid{position:absolute;left:14px;top:74px;width:250px;height:222px;display:grid;grid-template-columns:1fr 1fr;grid-template-rows:1fr 1fr 1fr}
  .benefit{display:flex;flex-direction:column;align-items:center;justify-content:flex-end;padding-bottom:4px;font-size:9px;text-align:center;line-height:1.15}
  .benefit svg{margin-bottom:6px}
  .benefit:nth-child(odd){border-right:2px dotted var(--teal)}
  .benefit:nth-child(-n+4){border-bottom:2px dotted var(--teal)}
  .footer{left:0;bottom:0;width:100%;height:64px;background:var(--ink)}
  .footer__wave{position:absolute;left:0;top:0}
  .footer__phone{left:24px;top:15px;display:flex;align-items:center;gap:12px;color:var(--white);font-size:22px;font-weight:500}
  .footer__phone svg{flex:0 0 auto}
  .footer__address{right:14px;top:9px;text-align:right;color:var(--white);font-size:10.5px;line-height:1.4}
  .footer__address span{display:inline-flex;align-items:center;gap:4px}
  .footer__brand{left:60px;top:18px;width:140px;text-align:center;color:var(--white)}

  /* Brain flyer */
  .brain-body{left:0;top:125px;width:537px;height:575px;background:linear-gradient(180deg,#93dbe0 0%,#d8f3f4 45%,#ffffff 75%)}
  .brain-top{left:0;top:0}
  .partner{left:14px;top:26px;display:flex;align-items:center;gap:8px;font-size:11px;font-weight:500;color:#3b3d40}
  .partner__dot{width:36px;height:36px;border-radius:50%;border:3px solid #8a8c90}
  .call{left:254px;top:4px;display:flex;align-items:center;gap:10px;color:var(--white)}
  .call__lead{font-size:30px;line-height:1}
  .call__num{font-size:20px;font-weight:700;letter-spacing:.5px}
  .about{right:17px;top:47px;text-align:right;font-size:10px;line-height:1.25;white-space:nowrap}
  .brain-badge{width:108px;height:108px;border-radius:50%}
  .brain-badge--boost{left:77px;top:140px;background:var(--teal);padding:9px}
  .brain-badge--boost div{width:100%;height:100%;border-radius:50%;background:var(--ink)}
  .brain-badge--bust{left:345px;top:140px;background:var(--teal);border:6px solid var(--ink)}
  .brain-title{left:195px;top:148px;width:150px;text-align:center;line-height:.95}
  .brain-title span{display:block;font-size:34px;color:var(--teal-dark)}
  .brain-title span:last-child{color:var(--ink)}
  .arrows{left:0;top:0}
  .col-title{font-size:21px;font-weight:700;text-align:center;line-height:1.05;letter-spacing:.3px}
  .col-title--boost{left:40px;top:286px;width:195px;color:var(--ink)}
  .col-title--bust{left:310px;top:282px;width:180px;color:var(--teal)}
  .bust-rule{left:345px;top:330px;width:110px;border-top:2px dotted var(--teal)}
  .tips{display:flex;flex-direction:column}
  .tips--boost{left:52px;top:342px;width:168px;gap:7px;color:var(--ink)}
  .tips--bust{left:318px;top:341px;width:168px;gap:6px;color:var(--white)}
  .tip{display:flex;gap:8px;align-items:flex-start}
  .tip__icon{flex:0 0 24px;height:24px;border-radius:50%;border:1.5px solid currentColor;margin-top:1px}
  .tip__name{font-size:8.4px;font-weight:700;line-height:1.15}
  .tip__note{font-size:7px;font-style:italic;line-height:1.25}
</style>
</head>
<body>
<div class="canvas">

  <!-- Home care flyer -->
  <section class="flyer flyer--homecare">
    <div class="abs hero-photo" role="img" aria-label="Photo of four care team members in masks standing on a park path in winter"></div>
    <svg class="abs header-art" width="538" height="140" viewBox="0 0 538 140" aria-hidden="true">
      <path d="M0 0H538V74C430 62 330 80 230 112L0 112Z" fill="#5cc4c9"/>
      <path d="M215 122C320 78 440 66 538 74V90C440 82 330 96 235 132Z" fill="#ffffff"/>
      <ellipse cx="70" cy="-10" rx="162" ry="148" fill="#111213" stroke="#5cc4c9" stroke-width="5"/>
      <path d="M405 84C440 80 480 79 530 82" stroke="#2a9aa0" stroke-width="2" fill="none"/>
    </svg>
    <div class="abs brand-mark">
      <div class="brand-mark__name">ALDERLINE</div>
      <div class="brand-mark__sub">HEALTHCARE</div>
    </div>
    <div class="abs home-title script">Home Care</div>

    <p class="abs vision">The Alderline HealthCare vision is to identify and meet the needs of our patients, business associates, and employees, and to provide premier quality, cost effective services that exceed the expectations of those we serve, while providing opportunities for our employees to flourish in their careers.</p>

    <div class="abs audience">
      <div class="audience__lead script">Who is</div>
      <div class="audience__title">RECEIVING HOMECARE?</div>
      <svg class="audience__rule" width="150" height="6" viewBox="0 0 150 6" aria-hidden="true"><path d="M2 4C50 1 100 1 148 4" stroke="#5cc4c9" stroke-width="2" fill="none"/></svg>
      <div class="audience__people">PEOPLE</div>
      <div class="audience__list">
        <em>MANAGING</em> Chronic Conditions<br>
        <em>RECOVERING</em> from Acute Illness<br>
        with <em>DEMENTIA</em><br>
        plus <em>OLDER ADULTS</em>
      </div>
    </div>
    <div class="abs care-illustration" role="img" aria-label="Illustration of caring hands holding an elderly couple, with patients and caregivers above"></div>

    <div class="abs benefits">
      <div class="benefits__head">
        <div class="benefits__lead script">Benefits</div>
        <div class="benefits__title">OF ALDERLINE HOMECARE</div>
      </div>
      <div class="benefits__grid">
        <div class="benefit">
          <svg width="60" height="30" viewBox="0 0 60 30" aria-hidden="true"><path d="M8 4V16H3L11 26L19 16H14V4Z" fill="#5cc4c9"/><path d="M30 14L44 2H56V14L42 28Z" fill="#5cc4c9"/><circle cx="51" cy="7" r="2" fill="#111213"/></svg>
          LOWER COSTS
        </div>
        <div class="benefit">
          <svg width="30" height="32" viewBox="0 0 30 32" aria-hidden="true"><rect x="6" y="10" width="18" height="16" rx="4" fill="#5cc4c9"/><rect x="9" y="26" width="12" height="5" fill="#5cc4c9"/><path d="M6 2L9 6M15 0V5M24 2L21 6" stroke="#5cc4c9" stroke-width="2"/></svg>
          PRESERVES AUTONOMY
        </div>
        <div class="benefit">
          <svg width="60" height="34" viewBox="0 0 60 34" aria-hidden="true"><g fill="#5cc4c9"><circle cx="12" cy="8" r="5"/><rect x="6" y="14" width="12" height="18" rx="3"/><circle cx="30" cy="6" r="6"/><rect x="23" y="13" width="14" height="21" rx="3"/><circle cx="48" cy="8" r="5"/><rect x="42" y="14" width="12" height="18" rx="3"/></g></svg>
          PRESERVES SOCIAL TIES
        </div>
        <div class="benefit">
          <svg width="40" height="34" viewBox="0 0 40 34" aria-hidden="true"><g fill="#5cc4c9"><circle cx="15" cy="9" r="8"/><path d="M0 34C0 22 6 18 15 18S30 22 30 34Z"/><rect x="29" y="19" width="4" height="14"/><rect x="24" y="24" width="14" height="4"/></g></svg>
          ENCOURAGES<br>PATIENT CENTEREDNESS
        </div>
        <div class="benefit">
          <svg width="60" height="32" viewBox="0 0 60 32" aria-hidden="true"><path d="M8 4V16H3L11 26L19 16H14V4Z" fill="#5cc4c9"/><path d="M42 2L58 30H26Z" fill="#5cc4c9"/><rect x="40.5" y="11" width="3" height="10" fill="#111213"/><rect x="40.5" y="23" width="3" height="3" fill="#111213"/></svg>
          REDUCES RISK<br>SOME COMPLICATIONS
        </div>
        <div class="benefit">
          <svg width="34" height="34" viewBox="0 0 34 34" aria-hidden="true"><circle cx="13" cy="13" r="10" stroke="#5cc4c9" stroke-width="3" fill="none"/><path d="M20 20L31 31" stroke="#5cc4c9" stroke-width="4" stroke-linecap="round"/></svg>
          ALLOWS FOR ASSESSMENT<br>OF SOCIAL DETERMINANTS<br>OF HEALTH
        </div>
      </div>
    </div>

    <footer class="abs footer">
      <svg class="footer__wave" width="538" height="64" viewBox="0 0 538 64" aria-hidden="true">
        <path d="M210 64C290 20 400 4 538 2V64Z" fill="#5cc4c9"/>
      </svg>
      <div class="abs footer__phone">
        <svg width="34" height="34" viewBox="0 0 24 24" aria-hidden="true"><path d="M6.6 10.8a15 15 0 0 0 6.6 6.6l2.2-2.2c.3-.3.7-.4 1-.2 1.1.4 2.3.6 3.6.6.6 0 1 .4 1 1V20c0 .6-.4 1-1 1C10.6 21 3 13.4 3 4c0-.6.4-1 1-1h3.5c.6 0 1 .4 1 1 0 1.3.2 2.5.6 3.6.1.3 0 .7-.2 1Z" fill="#5cc4c9"/></svg>
        <span>555.014.2200</span>
      </div>
      <div class="abs footer__address">
        <span>48 Larkspur Ave, <svg width="10" height="10" viewBox="0 0 10 10" aria-hidden="true"><circle cx="5" cy="5" r="5" fill="#fff"/><circle cx="5" cy="4" r="1.8" fill="#111213"/></svg></span><br>
        Suite 300, Fenwick, WI 53999<br>
        <span>WWW.ALDERLINEHEALTH.COM <svg width="10" height="10" viewBox="0 0 10 10" aria-hidden="true"><circle cx="5" cy="5" r="5" fill="#fff"/><circle cx="5" cy="5" r="2.5" fill="none" stroke="#111213"/></svg></span>
      </div>
    </footer>
  </section>

  <!-- Brain health flyer -->
  <section class="flyer flyer--brain">
    <div class="abs brain-body"></div>
    <svg class="abs brain-top" width="537" height="135" viewBox="0 0 537 135" aria-hidden="true">
      <path d="M205 0H537V130H0V122C110 118 185 78 205 0Z" fill="#5cc4c9"/>
      <path d="M203 0H537V42H196C200 30 202 15 203 0Z" fill="#111213"/>
    </svg>
    <div class="abs partner"><span class="partner__dot"></span>Quillmere Vista Center</div>
    <div class="abs call">
      <span class="call__lead script">Call Us</span>
      <svg width="24" height="24" viewBox="0 0 24 24" aria-hidden="true"><path d="M6.6 10.8a15 15 0 0 0 6.6 6.6l2.2-2.2c.3-.3.7-.4 1-.2 1.1.4 2.3.6 3.6.6.6 0 1 .4 1 1V20c0 .6-.4 1-1 1C10.6 21 3 13.4 3 4c0-.6.4-1 1-1h3.5c.6 0 1 .4 1 1 0 1.3.2 2.5.6 3.6.1.3 0 .7-.2 1Z" fill="#5cc4c9"/></svg>
      <span class="call__num">555.014.2200</span>
    </div>
    <p class="abs about">Quillmere Vista Center is a non-profit organization stemming<br>from the merger of NRBS (Northridge Brain Recovery Society)<br>and HBRS (Halden Brain Relearning Society).<br>Quillmere Vista Center offers programs and services at no cost to adults<br>who have sustained an acquired brain injury, and their families.<br>Services are offered from offices in Halden and Northridge.</p>

    <div class="abs brain-badge brain-badge--boost"><div role="img" aria-label="Brain icon surrounded by rays"></div></div>
    <div class="abs brain-badge brain-badge--bust" role="img" aria-label="Brain icon struck by lightning bolts"></div>
    <div class="abs brain-title script"><span>Keeping</span><span>Your Brain</span><span>Healthy</span></div>

    <svg class="abs arrows" width="537" height="762" viewBox="0 0 537 762" aria-hidden="true">
      <path d="M137 258L262 337H225V670Q225 685 210 685H56Q41 685 41 670V337H12Z" fill="#5cc4c9"/>
      <path d="M322 258H476Q491 258 491 273V606H525L400 686L274 606H307V273Q307 258 322 258Z" fill="#111213"/>
    </svg>
    <div class="abs col-title col-title--boost">BRAIN<br>BOOSTERS</div>
    <div class="abs col-title col-title--bust">BRAIN<br>BUSTERS</div>
    <div class="abs bust-rule"></div>

    <ul class="abs tips tips--boost">
      <li class="tip"><span class="tip__icon" role="img" aria-label="Wheat icon"></span><div><div class="tip__name">OPT FOR WHOLEGRAINS</div><div class="tip__note">The brain needs energy</div></div></li>
      <li class="tip"><span class="tip__icon" role="img" aria-label="Fish icon"></span><div><div class="tip__name">EAT OILY FISH</div><div class="tip__note">Essential fatty acids can't be made<br>by the body</div></div></li>
      <li class="tip"><span class="tip__icon" role="img" aria-label="Blueberries icon"></span><div><div class="tip__name">BINGE ON BLUEBERRIES</div><div class="tip__note">Effective in delaying<br>short term memory loss</div></div></li>
      <li class="tip"><span class="tip__icon" role="img" aria-label="Tomato icon"></span><div><div class="tip__name">EAT MORE TOMATOES</div><div class="tip__note">Protect against the kind of free radical damage which occurs in the development of dementia.</div></div></li>
      <li class="tip"><span class="tip__icon" role="img" aria-label="Vitamins icon"></span><div><div class="tip__name">ADD VITALITY WITH VITAMINS</div><div class="tip__note">B6, B12 &amp; folic acid are known to reduce levels of homocysteine in the blood</div></div></li>
      <li class="tip"><span class="tip__icon" role="img" aria-label="Blackcurrant icon"></span><div><div class="tip__name">GET A BLACKCURRANT BOOST</div><div class="tip__note">Increase mental agility</div></div></li>
      <li class="tip"><span class="tip__icon" role="img" aria-label="Pumpkin icon"></span><div><div class="tip__name">PICK UP ON PUMPKIN SEEDS</div><div class="tip__note">(Zinc) Enhancing memory and thinking skills</div></div></li>
      <li class="tip"><span class="tip__icon" role="img" aria-label="Broccoli icon"></span><div><div class="tip__name">BET ON BROCCOLI</div><div class="tip__note">(Vit K) Enhance cognitive<br>function &amp; improve brain power</div></div></li>
      <li class="tip"><span class="tip__icon" role="img" aria-label="Nuts icon"></span><div><div class="tip__name">GO NUTS</div><div class="tip__note">(Vit E) Prevent cognitive decline</div></div></li>
    </ul>

    <ul class="abs tips tips--bust">
      <li class="tip"><span class="tip__icon" role="img" aria-label="Drumstick icon"></span><div><div class="tip__name">FATTY FAST FOODS</div><div class="tip__note">Connected with brain shrinkage<br>that can lead to Alzheimer's</div></div></li>
      <li class="tip"><span class="tip__icon" role="img" aria-label="Salt shaker icon"></span><div><div class="tip__name">SALTY FOODS</div><div class="tip__note">They are hard on the brain</div></div></li>
      <li class="tip"><span class="tip__icon" role="img" aria-label="Processed food icon"></span><div><div class="tip__name">PROCESSED FOODS</div><div class="tip__note">Artificial food additives affect the cognitive functioning &amp; behaviour of some children</div></div></li>
      <li class="tip"><span class="tip__icon" role="img" aria-label="Frying pan icon"></span><div><div class="tip__name">FRIED FOODS</div><div class="tip__note">Raised the risk of neurologic degenerative diseases like Alzheimer's &amp; Parkinson's</div></div></li>
      <li class="tip"><span class="tip__icon" role="img" aria-label="Pesticide icon"></span><div><div class="tip__name">FOODS W/ PESTICIDE RESIDUE</div><div class="tip__note">Affect children's IQ &amp; on preterm birth &amp; ADHD</div></div></li>
      <li class="tip"><span class="tip__icon" role="img" aria-label="Pill bottle icon"></span><div><div class="tip__name">DOZALIN PM</div><div class="tip__note">Cloud your brain</div></div></li>
      <li class="tip"><span class="tip__icon" role="img" aria-label="No alcohol icon"></span><div><div class="tip__name">ALCOHOL</div><div class="tip__note">In excess will cloud your memory</div></div></li>
      <li class="tip"><span class="tip__icon" role="img" aria-label="Sweetener icon"></span><div><div class="tip__name">ARTIFICIAL SWEETENERS</div><div class="tip__note">Bad for memory</div></div></li>
      <li class="tip"><span class="tip__icon" role="img" aria-label="Burger icon"></span><div><div class="tip__name">JUNK FOOD</div><div class="tip__note">Bad for brain</div></div></li>
    </ul>

    <footer class="abs footer">
      <svg class="footer__wave" width="537" height="65" viewBox="0 0 537 65" aria-hidden="true">
        <path d="M210 65C290 22 400 5 537 3V65Z" fill="#5cc4c9"/>
      </svg>
      <div class="abs footer__brand">
        <div class="brand-mark__name">ALDERLINE</div>
        <div class="brand-mark__sub">HEALTHCARE</div>
      </div>
      <div class="abs footer__address">
        <span>48 Larkspur Ave, <svg width="10" height="10" viewBox="0 0 10 10" aria-hidden="true"><circle cx="5" cy="5" r="5" fill="#fff"/><circle cx="5" cy="4" r="1.8" fill="#111213"/></svg></span><br>
        Suite 300, Fenwick, WI 53999<br>
        <span>WWW.ALDERLINEHEALTH.COM <svg width="10" height="10" viewBox="0 0 10 10" aria-hidden="true"><circle cx="5" cy="5" r="5" fill="#fff"/><circle cx="5" cy="5" r="2.5" fill="none" stroke="#111213"/></svg></span>
      </div>
    </footer>
  </section>

</div>
</body>
</html>
```